Brightwell Essence colloidal silver spray for pets.

We need a label for an 8-oz cobalt blue spray bottle. We are a small company just starting to share the benefits of colloidal silver. Our first offering will be the 8-oz spray bottle for pets. We would also like to update our logo. The finished project should be crisp and incorporate a dog on the label. I have attached the information we would like on the label and our logo, which can be changed to match your vision.
Updates

Hi, I would like to remind you that we are using a cobalt blue bottle with a black sprayer and would like an updated logo. Also, for the business cards, we don't want an animal on them, as we are planning future products for people. thank you

```html
<!DOCTYPE html>
<html lang="en">
<head>
<meta charset="UTF-8">
<title>Colloidal Silver – Natural First Aid for Pets Label</title>
<link rel="stylesheet" href="https://fonts.googleapis.com/css2?family=Montserrat:wght@400;500;600;700;800&display=swap">
<style>
  :root {
    --page-bg: #f3efec;
    --label-pink: #eba7ab;
    --label-pink-deep: #c86f7c;
    --label-pink-soft: #f3c3c4;
    --ink-dark: #333033;
    --ink-white: #ffffff;
    --silver: #e6e6e8;
    --illustration-tone: #d9925f;
  }
  * { margin: 0; padding: 0; box-sizing: border-box; }
  html, body {
    width: 1200px;
    height: 1200px;
    overflow: hidden;
    background: var(--page-bg);
  }
  .canvas {
    position: relative;
    width: 1200px;
    height: 1200px;
    display: flex;
    align-items: center;
    justify-content: center;
  }
  .label {
    position: relative;
    width: 840px;
    height: 1120px;
    background: var(--label-pink);
    overflow: hidden;
    font-family: "Montserrat", sans-serif;
  }
  .label-swoosh {
    position: absolute;
    inset: 0;
    width: 100%;
    height: 100%;
  }
  .product-name {
    position: absolute;
    left: 112px;
    top: 190px;
    width: 620px;
    text-align: center;
    color: var(--ink-white);
  }
  .product-name-top {
    display: block;
    font-weight: 500;
    font-size: 86px;
    line-height: 1;
    letter-spacing: 1px;
  }
  .product-name-main {
    display: block;
    margin-top: 6px;
    font-weight: 800;
    font-size: 164px;
    line-height: 1;
    letter-spacing: 2px;
    color: var(--silver);
    -webkit-text-stroke: 6px var(--ink-dark);
    paint-order: stroke fill;
  }
  .tagline {
    position: absolute;
    left: 52px;
    top: 445px;
    width: 743px;
    height: 80px;
    background: var(--ink-white);
    color: var(--ink-dark);
    display: flex;
    align-items: center;
    justify-content: center;
    font-weight: 600;
    font-size: 42px;
    letter-spacing: 1px;
    box-shadow: 0 3px 6px rgba(0,0,0,0.18);
  }
  .mascot {
    position: absolute;
    left: 0;
    top: 560px;
    width: 300px;
    height: 455px;
    border-radius: 44% 50% 40% 46%;
    background: radial-gradient(ellipse at 50% 40%, #f4e7dd 0%, var(--illustration-tone) 62%, rgba(217,146,95,0) 78%);
  }
  .strength {
    position: absolute;
    left: 343px;
    top: 735px;
    color: var(--ink-white);
    font-weight: 700;
    font-size: 38px;
    letter-spacing: 1px;
  }
  .claims {
    position: absolute;
    left: 343px;
    top: 818px;
    color: var(--ink-white);
    font-weight: 400;
    font-size: 25px;
    line-height: 1.3;
    list-style: none;
  }
  .purity-seal {
    position: absolute;
    left: 670px;
    top: 545px;
    width: 186px;
    height: 186px;
  }
  .purity-seal text {
    font-family: "Montserrat", sans-serif;
    font-weight: 800;
    fill: var(--label-pink-deep);
  }
</style>
</head>
<body>
  <main class="canvas">
    <section class="label">
      <svg class="label-swoosh" viewBox="0 0 840 1120" preserveAspectRatio="none" aria-hidden="true">
        <path d="M0 1060 C 260 1040, 560 960, 840 810 L 840 1120 L 0 1120 Z" fill="var(--label-pink-deep)"/>
        <path d="M0 1085 C 300 1075, 600 1010, 840 900 L 840 1120 L 0 1120 Z" fill="var(--label-pink)"/>
        <path d="M0 1060 C 260 1040, 560 960, 840 810 L 840 835 C 580 975, 280 1052, 0 1072 Z" fill="var(--label-pink-soft)" opacity="0.5"/>
      </svg>

      <h1 class="product-name">
        <span class="product-name-top">COLLOIDAL</span>
        <span class="product-name-main">SILVER</span>
      </h1>

      <p class="tagline">NATURAL FIRST AID FOR PETS</p>

      <div class="mascot" role="img" aria-label="Cartoon illustration of a happy brown and white puppy running"></div>

      <p class="strength">10 PPM</p>
      <ul class="claims">
        <li>No preservatives</li>
        <li>No additives</li>
      </ul>

      <svg class="purity-seal" viewBox="0 0 186 186" role="img" aria-label="100% pure seal">
        <path fill="var(--label-pink-soft)" stroke="#ffffff" stroke-width="4"
          d="M93 8 L106 20 L123 14 L131 30 L149 31 L151 49 L167 58 L161 75 L172 90 L161 104 L167 121 L151 130 L149 148 L131 149 L123 165 L106 159 L93 172 L80 159 L63 165 L55 149 L37 148 L35 130 L19 121 L25 104 L14 90 L25 75 L19 58 L35 49 L37 31 L55 30 L63 14 L80 20 Z"/>
        <text x="93" y="88" text-anchor="middle" font-size="34">100%</text>
        <text x="93" y="120" text-anchor="middle" font-size="28">PURE</text>
      </svg>
    </section>
  </main>
</body>
</html>
```